Visitenkarten-Design für Eventcatering & Gemeinschaftsverpflegung
Zielgruppe
Wir sind ein kreatives und aufstrebendes Unternehmen.
Seit jahren sind wir im Eventcatering und der Gemeinschaftsverpflegung tätig.
Als Marktführer kochen wir super leckeres Mittagessen für Grundschulen und Kindertagesstätten in Berlin und Brandenburg und bewirtschaften mehrere Betriebsrestaurants.
Wir sind sehr krativ und bleiben nie stehen, so bereichern wir die Gastronomie in allen
Bereichen mit immer neuen innovativen Ideen und der Leidenschaft zum gesunden und leckeren Essen.
We are a creative and ambitious company.
We have been active in event catering and community catering for years.
As the market leader, we cook delicious lunches for elementary schools and day-care centers in Berlin and Brandenburg and we run several company restaurants.
We are very creative and never stand still, this is how we enrich the gastronomy in all of them
areas with new, innovative ideas and a passion for healthy and delicious food.
Aufgabenstellung
Wir möchten gern die Rottöne aus unserem Logo wiederfinden.
Unser Logo darf im Vordergrund stehen.
We would like to find the red tones from our logo again.
Our logo can be in the foreground.

```html
<!DOCTYPE html>
<html lang="de">
<head>
<meta charset="utf-8">
<title>Tafelwerk Catering – Visitenkarte</title>
<link rel="stylesheet" href="https://fonts.googleapis.com/css2?family=Montserrat:wght@400;600&display=swap">
<style>
  :root {
    --bg: #2e2e30;
    --card: #ffffff;
    --red: #e3122b;
    --ink: #2b2b2b;
    --grey: #6f6f73;
    --wood-1: #b06a35;
    --wood-2: #d49a5e;
    --food-1: #e9c46a;
    --food-2: #c83a2a;
  }
  * { box-sizing: border-box; margin: 0; padding: 0; }
  html, body { width: 1200px; height: 900px; overflow: hidden; }
  body {
    background: var(--bg);
    font-family: "Montserrat", sans-serif;
    display: flex;
    align-items: center;
    justify-content: center;
    gap: 40px;
  }
  .card {
    position: relative;
    width: 540px;
    height: 348px;
    background: var(--card);
    box-shadow: 0 10px 30px rgba(0,0,0,.45);
    overflow: hidden;
  }
  .brand {
    display: flex;
    align-items: center;
    gap: 10px;
  }
  .brand-mark {
    width: 26px;
    height: 26px;
    background: var(--red);
  }
  .brand-name {
    font-weight: 600;
    font-size: 22px;
    color: var(--ink);
    letter-spacing: .2px;
  }
  /* contact side */
  .contact .brand { position: absolute; left: 40px; top: 44px; }
  .contact .brand-name { font-size: 19px; }
  .contact .brand-mark { width: 22px; height: 22px; }
  .person {
    position: absolute;
    left: 300px;
    top: 118px;
    padding-left: 18px;
  }
  .person::before {
    content: "";
    position: absolute;
    left: -4px;
    top: -8px;
    width: 3px;
    height: 44px;
    background: var(--red);
  }
  .person-name { font-size: 17px; color: var(--ink); }
  .person-name strong { color: var(--red); font-weight: 600; }
  .person-role { font-size: 11px; color: var(--grey); margin-top: 2px; }
  .details {
    position: absolute;
    left: 300px;
    top: 182px;
    list-style: none;
    font-size: 12.5px;
    line-height: 17px;
    color: var(--grey);
  }
  .details li { display: flex; align-items: flex-start; gap: 8px; }
  .details svg { width: 12px; height: 12px; margin-top: 3px; flex: none; fill: var(--red); }
  .details .address { margin-bottom: 14px; }
  /* photo side */
  .photo {
    position: absolute;
    inset: 0;
    background:
      radial-gradient(ellipse at 35% 40%, var(--food-1) 0%, rgba(233,196,106,0) 45%),
      radial-gradient(ellipse at 30% 15%, var(--food-2) 0%, rgba(200,58,42,0) 35%),
      linear-gradient(135deg, var(--wood-2), var(--wood-1));
  }
  .logo-panel {
    position: absolute;
    left: 300px;
    top: 100px;
    width: 240px;
    height: 150px;
    background: var(--card);
    display: flex;
    align-items: center;
    justify-content: center;
  }
</style>
</head>
<body>
  <section class="card contact">
    <div class="brand">
      <span class="brand-mark"></span>
      <span class="brand-name">Tafelwerk Catering</span>
    </div>
    <div class="person">
      <p class="person-name">Jonas <strong>Kellner</strong></p>
      <p class="person-role">Inhaber</p>
    </div>
    <ul class="details">
      <li class="address">
        <svg viewBox="0 0 12 12"><path d="M6 0a4 4 0 0 0-4 4c0 3 4 8 4 8s4-5 4-8a4 4 0 0 0-4-4zm0 5.5A1.5 1.5 0 1 1 6 2.5a1.5 1.5 0 0 1 0 3z"/></svg>
        <span>Birkenweg 27<br>A-4120 Neudorfen</span>
      </li>
      <li>
        <svg viewBox="0 0 12 12"><path d="M2.5 0.5l2 2.5-1 1.2a6.5 6.5 0 0 0 4.3 4.3l1.2-1 2.5 2-1.2 2A9.5 9.5 0 0 1 .5 1.7z"/></svg>
        <span>01234/567 80-21</span>
      </li>
      <li>
        <svg viewBox="0 0 12 12"><path d="M3 0h5v3H3zM1 4h10v5H9v3H3V9H1zm3 5v2h4V9z"/></svg>
        <span>01234/567 80-31</span>
      </li>
      <li>
        <svg viewBox="0 0 12 12"><path d="M0 2h12v8H0zm1 1v.4l5 3.3 5-3.3V3z"/></svg>
        <span>info@tafelwerk-catering.de</span>
      </li>
      <li>
        <svg viewBox="0 0 12 12"><circle cx="6" cy="6" r="5.5"/><path d="M.5 6h11M6 .5c-2.5 3-2.5 8 0 11M6 .5c2.5 3 2.5 8 0 11" stroke="#fff" stroke-width=".8" fill="none"/></svg>
        <span>www.tafelwerk-catering.de</span>
      </li>
    </ul>
  </section>

  <section class="card front">
    <div class="photo" role="img" aria-label="Foto einer Holzplatte mit Obst, Gemüse, Käse und Walnüssen auf einem Holztisch"></div>
    <div class="logo-panel">
      <div class="brand">
        <span class="brand-mark"></span>
        <span class="brand-name">Tafelwerk Catering</span>
      </div>
    </div>
  </section>
</body>
</html>
```